Website for premium health insurance and concierge medicine

This is a brand new website for Vantor Insurance Services that specializes in Health Insurance and Concierge Medicine for high net-worth and affluent individuals and families. Through this website, clients will be able to learn about products and services, submit applications, and complete self enrollment forms. The website needs to have a premium look & feel that will appeal to a discerning high net-worth individual.

I’m looking for 4 pages in total to begin with. I’m also looking for a designer who will be interested in continuing to build out this new site further over the next few months.

The headline for each page is listed below:

Page 1: HOME PAGE
“Premium Healthcare | Bespoke Concierge Services | Absolute Peace of Mind.”

Page 2: HEALTH INSURANCE
“Premium Healthcare | Elevated.”

Page 3: CONCIERGE MEDICINE
“Personalized Medicine | At-Home Concierge Care | Your Private Physician, 24/7.”

Page 4: DENTAL & VISION
“Your Smile | Your Vision | Perfected.”

Here are several links to existing websites that can be used as design inspiration:

https://brevanwell.com
https://www.quemby.org/specialties-services/other-programs-services/concierge-medicine
https://physelmdkx.com

More generally speaking, I like a clean, modern, dutch style of websites. Here’s an unrelated site that has a good design:

https://www.ostravine.com

Here are a few additional phrases and keywords that will help inspire the design:

Premium Health Insurance
Executive Health Insurance
Concierge Medicine
24/7 access dedicated concierge team
Integrative Concierge Care

I will upload logo files below, here are the font & colors information:

Font: Trajan Pro Bold
Colors:
Blue: hex code: 0071BD, Rgb code: 0, 113, 189  cmyk code: 87,53,0,0
Gray: hex code: #666666, Rgb code: 102,102,102 cmyk code: 60,51,51,20

```html
<!DOCTYPE html>
<html lang="en">
<head>
<meta charset="utf-8">
<title>Vantor Insurance Services – Concierge Medicine</title>
<link href="https://fonts.googleapis.com/css2?family=Cinzel:wght@400;600;700&family=Jost:wght@400;500&display=swap" rel="stylesheet">
<style>
:root{
  --blue:#0071bd;
  --gray:#666666;
  --ink:#222222;
  --muted:#6f6f6f;
  --light:#eeeeee;
  --pale-blue:#c9e1f1;
  --dark:#2f2f2f;
  --white:#ffffff;
}
*{margin:0;padding:0;box-sizing:border-box}
html,body{width:1200px;height:3669px;overflow:hidden}
body{position:relative;background:var(--white);font-family:"Jost",sans-serif;color:var(--muted)}
.abs{position:absolute}
.serif{font-family:"Cinzel",serif;color:var(--ink)}
.accent{color:var(--blue)}

/* header */
.topbar{left:330px;top:0;width:870px;height:51px;background:var(--blue);clip-path:polygon(30px 0,100% 0,100% 100%,0 100%);color:var(--white);font-size:12px}
.topbar span{position:absolute;top:18px;display:flex;align-items:center;gap:8px}
.social{position:absolute;top:14px;display:flex;gap:7px;left:662px}
.social i{display:block;width:24px;height:24px;border-radius:50%;background:rgba(255,255,255,.35)}
.divline{left:272px;top:0;width:2px;height:124px;background:var(--blue);transform:skewX(-33deg);transform-origin:top}
.brand{left:112px;top:30px;font-family:"Cinzel",serif;font-weight:700;color:var(--blue);font-size:19px;line-height:1.15;display:flex;align-items:center;gap:10px}
.brand b{width:28px;height:28px;border-radius:50%;background:var(--blue);display:block}
.nav{left:407px;top:80px;display:flex;gap:21px;font-size:12px;color:var(--gray)}
.btn-contact{left:987px;top:68px;width:124px;height:38px;background:var(--blue);color:var(--white);font-size:13px;display:flex;align-items:center;justify-content:center}

/* hero */
.hero{left:0;top:124px;width:1200px;height:448px;background:linear-gradient(90deg,#e9e9e9 0%,#ececec 40%,#d5dbe2 65%,#b9c8d8 100%)}
.hero h1{position:absolute;left:90px;top:105px;font-family:"Cinzel",serif;font-weight:600;font-size:74px;line-height:72px;color:var(--ink)}

/* intro */
.mark{left:170px;top:680px;width:185px;height:130px;display:flex;align-items:center;justify-content:center;font-family:"Cinzel",serif;font-weight:700;font-size:36px;color:var(--blue)}
.intro-title{left:408px;top:664px;font-size:38px;line-height:40px;font-weight:600}
.intro-text{left:408px;top:762px;width:625px;font-size:13px;line-height:22px}

.section-title{left:0;width:1200px;text-align:center;font-family:"Cinzel",serif;font-weight:600;font-size:38px;color:var(--ink)}

.step{top:995px;width:220px;text-align:center}
.step .shield{width:120px;height:130px;margin:0 auto;background:var(--pale-blue);clip-path:polygon(0 0,50% 8%,100% 0,100% 55%,50% 100%,0 55%);display:flex;align-items:center;justify-content:center;padding-bottom:14px}
.step h3{font-family:"Cinzel",serif;font-weight:600;font-size:16px;color:var(--ink);margin-top:18px}
.step p{font-size:13px;line-height:19px;margin-top:3px}

/* highlights */
.highlights{left:0;top:1287px;width:1200px;height:575px;background:var(--light)}
.card{top:128px;width:240px;height:377px;background:var(--white);box-shadow:0 6px 18px rgba(0,0,0,.06)}
.card .photo{height:211px}
.card h3{font-family:"Cinzel",serif;font-weight:600;font-size:16px;line-height:22px;color:var(--ink);margin:18px 14px 6px}
.card p{font-size:11.5px;line-height:19.5px;margin:0 14px}

/* privilege */
.priv-title{left:105px;top:1982px;font-size:38px;line-height:40px;font-weight:600}
.priv-item{left:105px;width:400px}
.priv-item h3{font-family:"Cinzel",serif;font-weight:600;font-size:17px;color:var(--ink)}
.priv-item p{font-size:13px;line-height:22px}
.priv-photo{left:633px;top:1963px;width:465px;height:437px;background:linear-gradient(135deg,#e8eaec,#cfd5da 60%,#b9c2c8)}

/* faq */
.faq{left:184px;width:833px;background:var(--white);box-shadow:0 4px 16px rgba(0,0,0,.08);padding:0 28px}
.faq h4{font-family:"Cinzel",serif;font-weight:600;font-size:16px;color:var(--ink);display:flex;justify-content:space-between;align-items:center}
.faq p{font-size:13px;line-height:20px;margin-top:8px;width:730px}

/* footer */
.footer{left:0;top:3141px;width:1200px;height:528px;background:var(--dark);color:#dddddd}
.cta{left:131px;top:3017px;width:934px;height:250px;background:var(--blue);text-align:center;color:var(--white)}
.cta h2{font-family:"Cinzel",serif;font-weight:700;font-size:38px;line-height:40px;margin-top:40px}
.cta p{font-size:13px;margin-top:8px}
.cta a{display:inline-block;margin-top:20px;background:var(--white);color:var(--ink);font-size:13px;padding:12px 20px;text-decoration:none}
.f-brand{left:92px;top:3390px;font-family:"Cinzel",serif;font-weight:700;font-size:24px;color:var(--white);display:flex;align-items:center;gap:12px}
.f-brand b{width:30px;height:30px;border-radius:50%;background:var(--white);display:block}
.f-col h5{font-family:"Cinzel",serif;font-weight:600;font-size:20px;color:var(--white);margin-bottom:14px}
.f-col a{display:block;color:#dddddd;text-decoration:none;font-size:12px;line-height:31px}
.f-col .row{display:flex;gap:10px;font-size:12px;line-height:18px;margin-bottom:18px}
.news{width:257px;height:46px;background:#4a4a4a;display:flex;align-items:center;padding:0 16px;justify-content:space-between;font-size:12px}
.copy{left:0;top:3632px;width:1200px;text-align:center;font-size:13px;color:#dddddd}
.totop{left:1137px;top:3557px;width:40px;height:40px;background:var(--blue);display:flex;align-items:center;justify-content:center}
</style>
</head>
<body>

<header>
  <div class="abs divline"></div>
  <div class="abs topbar">
    <span style="left:42px">
      <svg width="12" height="10" viewBox="0 0 12 10"><rect x="0.5" y="0.5" width="11" height="9" fill="none" stroke="#fff"/><path d="M1 1l5 4 5-4" fill="none" stroke="#fff"/></svg>
      Email Address: info@vantormail.com</span>
    <span style="left:272px">
      <svg width="11" height="11" viewBox="0 0 12 12"><path d="M2 1l3 0 1 3-2 1c1 2 2 3 4 4l1-2 3 1 0 3c-6 0-10-4-10-10z" fill="#fff"/></svg>
      Phone Number: 555-410-2290</span>
    <span style="left:595px">Follow us:</span>
    <div class="social"><i></i><i></i><i></i><i></i></div>
  </div>
  <div class="abs brand"><b></b>Vantor<br>Insurance<br>Services</div>
  <nav class="abs nav">
    <span>In-Home Services</span><span>Shipped To You</span><span>Membership</span><span>Locations</span><span>About Us</span>
    <span style="margin-left:20px;display:flex;gap:22px;align-items:center">
      <svg width="18" height="16" viewBox="0 0 18 16"><path d="M1 1h3l2 9h9l2-6H5" fill="none" stroke="#666" stroke-width="1.3"/><circle cx="7" cy="14" r="1.3" fill="#666"/><circle cx="14" cy="14" r="1.3" fill="#666"/></svg>Cart</span>
  </nav>
  <div class="abs btn-contact">Contact Us</div>
</header>

<section class="abs hero">
  <div class="abs" role="img" aria-label="Physician in white coat with stethoscope holding a tablet while consulting a patient" style="left:520px;top:0;width:680px;height:448px;background:linear-gradient(90deg,rgba(230,230,230,0),rgba(190,205,220,.6))"></div>
  <h1>Personalized<br>Medicine...</h1>
</section>

<div class="abs mark">Vantor</div>
<h2 class="abs serif intro-title">Exclusive, <span class="accent">Personalized Care</span><br>Anytime You Need It:</h2>
<p class="abs intro-text">Embrace a new paradigm of healthcare with our Concierge Medicine services. At Vantor Insurance Services, we offer personalized medical care that revolves around your schedule, providing peace of mind with a private physician available around the clock.</p>

<h2 class="abs section-title" style="top:920px">How Concierge <span class="accent">Medicine</span> Works</h2>

<div class="abs step" style="left:200px">
  <div class="shield"><svg width="54" height="54" viewBox="0 0 54 54"><circle cx="27" cy="27" r="24" fill="none" stroke="#0071bd" stroke-width="2"/><path d="M27 40V20M27 20l-5 5M27 20l5 5M20 32h14" fill="none" stroke="#0071bd" stroke-width="2"/></svg></div>
  <h3>Direct Access</h3><p>24/7 communication with your<br>dedicated physician.</p>
</div>
<div class="abs step" style="left:490px">
  <div class="shield"><svg width="66" height="48" viewBox="0 0 66 48"><g fill="none" stroke="#0071bd" stroke-width="2"><circle cx="33" cy="14" r="7"/><circle cx="15" cy="12" r="6"/><circle cx="51" cy="12" r="6"/><path d="M21 42c0-10 6-15 12-15s12 5 12 15M4 34c0-8 5-12 11-12M62 34c0-8-5-12-11-12"/></g></svg></div>
  <h3>Join Our Membership</h3><p>Personalized onboarding and<br>health assessment.</p>
</div>
<div class="abs step" style="left:780px">
  <div class="shield"><svg width="60" height="50" viewBox="0 0 60 50"><g fill="none" stroke="#0071bd" stroke-width="2"><circle cx="12" cy="12" r="7"/><rect x="8" y="34" width="6" height="12"/><rect x="20" y="28" width="6" height="18"/><rect x="32" y="22" width="6" height="24"/><rect x="44" y="14" width="6" height="32"/><path d="M4 46h54M22 20l12-8 10 4 12-12"/></g></svg></div>
  <h3>On-Demand Care</h3><p>Home visits, specialist coordina<br>tion, and wellness planning.</p>
</div>

<section class="abs highlights">
  <h2 class="abs section-title" style="top:50px"><span class="accent">Service</span> Highlights</h2>
  <div class="abs card" style="left:100px">
    <div class="photo" role="img" aria-label="Doctor at desk reviewing a tablet with a colleague" style="background:linear-gradient(135deg,#5c6f86,#c9d2da)"></div>
    <h3>24/7 Physician<br>Access</h3><p>Direct communication with your dedicated physician anytime, ensur ing immediate medical attention when you need it most.</p>
  </div>
  <div class="abs card" style="left:353px">
    <div class="photo" role="img" aria-label="Masked physician meeting a patient at home" style="background:linear-gradient(135deg,#b7c3b0,#e3e3e0)"></div>
    <h3>At-Home Medical<br>Visits</h3><p>Comprehensive medical services delivered in the comfort and privacy of your home, office, or preferred location.</p>
  </div>
  <div class="abs card" style="left:606px">
    <div class="photo" role="img" aria-label="Doctor discussing a health plan with a patient at a desk" style="background:linear-gradient(135deg,#d9dee3,#a9b6c2)"></div>
    <h3>Preventive Health<br>Strategies</h3><p>Proactive and personalized health plans focusing on prevention and wellness, tailored to your individual health profile.</p>
  </div>
  <div class="abs card" style="left:859px">
    <div class="photo" role="img" aria-label="Team of specialists in scrubs consulting together" style="background:linear-gradient(135deg,#cfdbe6,#8aa3bc)"></div>
    <h3>Coordinated<br>Specialist Care</h3><p>Seamless referrals and priority access to a network of leading specialists and medical institutions.</p>
  </div>
</section>

<h2 class="abs serif priv-title">Member <span class="accent">Privilege</span><br>Always Here for You</h2>
<div class="abs priv-item" style="top:2082px"><h3>Exclusive Health Assessments</h3><p>In-depth evaluations and executive physicals to proactively<br>manage and enhance your health.</p></div>
<div class="abs priv-item" style="top:2177px"><h3>Customized Wellness Plans</h3><p>Personalized programs encompassing nutrition, fitness, and<br>lifestyle modifications to achieve optimal health outcomes.</p></div>
<div class="abs priv-item" style="top:2273px"><h3>Holistic Wellness Programs</h3><p>Integrative concierge care that combines traditional<br>medicine with alternative therapies for a balanced<br>approach to health.</p></div>
<div class="abs priv-photo" role="img" aria-label="Physician explaining a report to a patient in a clinic office"></div>

<h2 class="abs section-title" style="top:2488px">FAQs</h2>
<div class="abs faq" style="top:2562px;height:103px;padding-top:22px">
  <h4>1. What is concierge medicine? <svg width="12" height="8" viewBox="0 0 12 8"><path d="M1 1l5 5 5-5" fill="none" stroke="#0071bd" stroke-width="2"/></svg></h4>
  <p>Concierge medicine offers personalized healthcare with direct access to your physician, 24/7 communication same day appointments, and even home visits, providing a more attentive and tailored healthcare experience.</p>
</div>
<div class="abs faq" style="top:2672px;height:55px;padding-top:18px"><h4>2. How does concierge medicine differ from traditional healthcare? <svg width="12" height="8" viewBox="0 0 12 8"><path d="M1 7l5-5 5 5" fill="none" stroke="#0071bd" stroke-width="2"/></svg></h4></div>
<div class="abs faq" style="top:2732px;height:55px;padding-top:18px"><h4>3. Is concierge medicine covered by insurance? <svg width="12" height="8" viewBox="0 0 12 8"><path d="M1 7l5-5 5 5" fill="none" stroke="#0071bd" stroke-width="2"/></svg></h4></div>
<div class="abs faq" style="top:2792px;height:55px;padding-top:18px"><h4>4. Can I contact my physician outside office hours? <svg width="12" height="8" viewBox="0 0 12 8"><path d="M1 7l5-5 5 5" fill="none" stroke="#0071bd" stroke-width="2"/></svg></h4></div>
<div class="abs faq" style="top:2852px;height:55px;padding-top:18px"><h4>5. Who benefits most from concierge medicine? <svg width="12" height="8" viewBox="0 0 12 8"><path d="M1 7l5-5 5 5" fill="none" stroke="#0071bd" stroke-width="2"/></svg></h4></div>

<footer class="abs footer"></footer>
<section class="abs cta">
  <h2>Your Health, Your Way Always<br>Within Reach.</h2>
  <p>Experience premium healthcare tailored to your lifestyle.</p>
  <a href="#">Schedule a Consultation</a>
</section>

<div class="abs f-brand"><b></b>Vantor Insurance<br>Services</div>
<div class="abs f-col" style="left:360px;top:3322px">
  <h5>Quick Links</h5>
  <a href="#">Home</a><a href="#">About Us</a><a href="#">Specials</a><a href="#">Our Approach</a><a href="#">Results</a><a href="#">Contact Us</a>
</div>
<div class="abs f-col" style="left:588px;top:3322px">
  <h5>Contact Info</h5>
  <div class="row"><svg width="12" height="10" viewBox="0 0 12 10"><rect width="12" height="10" fill="#ddd"/></svg><span>Email:<br>hello@vantorcare.com</span></div>
  <div class="row"><svg width="12" height="12" viewBox="0 0 12 12"><path d="M2 1l3 0 1 3-2 1c1 2 2 3 4 4l1-2 3 1 0 3c-6 0-10-4-10-10z" fill="#ddd"/></svg><span>Phone:<br>+08 555 018 2240</span></div>
  <div class="row"><svg width="10" height="13" viewBox="0 0 10 13"><path d="M5 13C1 8 0 6 0 5a5 5 0 0110 0c0 1-1 3-5 8z" fill="#ddd"/><circle cx="5" cy="5" r="2" fill="#2f2f2f"/></svg><span>Location:<br>Some address line here<br>United Kingdom VX90 2ZQ</span></div>
</div>
<div class="abs f-col" style="left:851px;top:3322px">
  <h5>Newsletter</h5>
  <p style="font-size:12px;line-height:18px;margin-bottom:18px">Subscribe to our email address to<br>get the latest news.</p>
  <div class="news"><span style="display:flex;gap:10px;align-items:center"><svg width="12" height="10" viewBox="0 0 12 10"><rect width="12" height="10" fill="#ddd"/></svg>Enter Your Email</span>
  <svg width="16" height="16" viewBox="0 0 16 16"><path d="M1 8l14-7-4 14-3-6z" fill="#fff"/></svg></div>
</div>
<div class="abs totop"><svg width="12" height="14" viewBox="0 0 12 14"><path d="M6 13V2M1 7l5-5 5 5" fill="none" stroke="#fff" stroke-width="1.6"/></svg></div>
<p class="abs copy">© Copyright 2025, Vantor insurance services All Rights Reserved</p>

</body>
</html>
```